出産内祝いのはがきの作成をお願いします。通信欄(片面です。)、良いものであれば、複数採用いたします。何か質問があればご連絡ください。用紙は縦向きです
子供の名前と、体重、誕生日。メッセージ。
写真を入れる場合と入れない場合をお願いします。
はがきサイズ タテ

お世話になります。

スタッフの意見により決定いたしました。

素晴らしいご提案ありがとうございます。

今後ともよろしくお願いいたします。

```html
<!DOCTYPE html>
<html lang="ja">
<head>
<meta charset="utf-8">
<title>出産内祝い はがき</title>
<link rel="stylesheet" href="https://fonts.googleapis.com/css2?family=Noto+Serif+JP:wght@400;500;600&display=swap">
<style>
  :root {
    --paper: #f7e7f1;
    --frame: #ffffff;
    --ink: #1c1a1c;
    --message: #b0779c;
    --wreath-pink: #f2a9c9;
    --wreath-lilac: #c9a6dc;
    --wreath-gold: #f3cf4f;
    --photo-light: #f7e9e4;
    --photo-mid: #e9c9bc;
  }
  html, body {
    margin: 0;
    padding: 0;
    overflow: hidden;
  }
  .card {
    position: relative;
    width: 811px;
    height: 1200px;
    background: var(--paper);
    font-family: "Noto Serif JP", serif;
    color: var(--ink);
    overflow: hidden;
  }
  .card__frame {
    position: absolute;
    inset: 22px;
    border: 3px solid var(--frame);
    pointer-events: none;
  }
  .birth-info {
    position: absolute;
    top: 60px;
    left: 0;
    right: 0;
    text-align: center;
  }
  .birth-info__name {
    margin: 0;
    font-size: 60px;
    font-weight: 500;
    letter-spacing: 2px;
    line-height: 1.1;
  }
  .birth-info__weight {
    margin: 4px 0 0;
    font-size: 34px;
    line-height: 1.3;
  }
  .birth-info__date {
    margin: 0;
    font-size: 36px;
    line-height: 1.3;
  }
  .portrait {
    position: absolute;
    left: 55px;
    top: 260px;
    width: 700px;
    height: 700px;
  }
  .message {
    position: absolute;
    top: 950px;
    left: 0;
    right: 0;
    margin: 0;
    text-align: center;
    color: var(--message);
    font-size: 22px;
    line-height: 38px;
    letter-spacing: 1px;
  }
</style>
</head>
<body>
  <main class="card">
    <div class="card__frame"></div>

    <header class="birth-info">
      <h1 class="birth-info__name">花村 彩香</h1>
      <p class="birth-info__weight">3000g</p>
      <p class="birth-info__date">平成 23.10.1 生</p>
    </header>

    <svg class="portrait" viewBox="0 0 700 700" aria-hidden="false">
      <defs>
        <linearGradient id="wreath-tone" x1="0" y1="0" x2="1" y2="1">
          <stop offset="0" stop-color="var(--wreath-pink)"/>
          <stop offset="0.4" stop-color="var(--wreath-lilac)"/>
          <stop offset="0.7" stop-color="var(--wreath-gold)"/>
          <stop offset="1" stop-color="var(--wreath-pink)"/>
        </linearGradient>
        <radialGradient id="photo-tone" cx="0.5" cy="0.45" r="0.6">
          <stop offset="0" stop-color="var(--photo-light)"/>
          <stop offset="1" stop-color="var(--photo-mid)"/>
        </radialGradient>
      </defs>
      <circle class="portrait__wreath" cx="350" cy="350" r="300" fill="none"
              stroke="url(#wreath-tone)" stroke-width="70" opacity="0.75"
              role="img" aria-label="パステルカラーの花のリース"/>
      <circle class="portrait__photo" cx="350" cy="350" r="255"
              fill="url(#photo-tone)"
              role="img" aria-label="赤ちゃんの写真"/>
    </svg>

    <p class="message">
      この度はお気遣いをいただきまして<br>
      誠に有難うございました<br>
      母子ともに健やかに過ごしております<br>
      ささやかな気持ちを込めて御礼の品をお届け致します<br>
      今後ともよろしくお願いいたします
    </p>
  </main>
</body>
</html>
```